Sumvera financial services stationery design

We need business stationery designed with letterheads, business cards, with compliments and envelope for a business that offers tax and accounting services
Updates

Designs look the same

Target Market(s)

Small to medium businesses, individuals, Self managed superfunds

Industry/Entity Type

Business

Font styles to use
Serif
Other font styles liked:
• Atlanta

Colors
32a6d6
3277b5

Requirements
Must have
• Logo incorporated with all my stationery
• professional
Should not have
• Lots of colours
• Busy

```html
<!DOCTYPE html>
<html lang="en">
<head>
<meta charset="utf-8">
<title>Sumvera Financial Services – Stationery</title>
<link rel="stylesheet" href="https://fonts.googleapis.com/css2?family=Cormorant+Garamond:wght@500&family=Open+Sans:ital,wght@0,400;0,600;1,600&display=swap">
<style>
  :root {
    --brand-sky: #32a6d6;
    --brand-navy: #3277b5;
    --ink: #3a3a3a;
    --ink-soft: #6a6a6a;
    --paper: #ffffff;
    --paper-tint: #f5f6f7;
    --backdrop: #2f2f2f;
  }
  * { box-sizing: border-box; margin: 0; padding: 0; }
  html, body { width: 1200px; height: 1200px; overflow: hidden; }
  body {
    background: var(--backdrop);
    font-family: "Open Sans", sans-serif;
    color: var(--ink);
    position: relative;
  }
  .sheet {
    position: absolute;
    background: var(--paper);
    overflow: hidden;
  }
  .band {
    position: absolute; left: 0; right: 0; bottom: 0;
    background: var(--brand-sky);
  }
  .wordmark {
    display: flex; align-items: center; gap: 10px;
    font-family: "Cormorant Garamond", serif;
    font-weight: 500;
    color: var(--ink);
    letter-spacing: 0.02em;
    line-height: 1;
  }
  .wordmark .mark-square {
    display: block;
    background: var(--brand-navy);
  }
  .wordmark--white { color: #fff; }
  .wordmark--white .mark-square { background: #fff; }

  .icon { width: 10px; height: 10px; fill: var(--brand-navy); flex: none; }
  .contact-line { display: flex; align-items: center; gap: 6px; white-space: nowrap; }

  /* Envelope */
  .envelope { left: 40px; top: 40px; width: 560px; height: 280px; }
  .envelope .wordmark { position: absolute; left: 40px; top: 104px; font-size: 40px; }
  .envelope .wordmark .mark-square { width: 30px; height: 30px; }
  .envelope .return-address { position: absolute; left: 40px; bottom: 34px; font-size: 11px; color: var(--ink-soft); }
  .envelope .band { height: 14px; }

  /* Compliments slip */
  .compliments { left: 40px; top: 360px; width: 560px; height: 264px; background: var(--paper-tint); }
  .compliments .wordmark { position: absolute; left: 40px; top: 44px; font-size: 44px; }
  .compliments .wordmark .mark-square { width: 34px; height: 34px; }
  .compliments .slip-title {
    position: absolute; left: 40px; bottom: 44px;
    font-size: 26px; letter-spacing: 0.12em; color: var(--brand-navy); font-weight: 400;
  }
  .compliments .slip-contacts {
    position: absolute; right: 40px; top: 118px;
    display: flex; gap: 18px; font-size: 11px; color: var(--ink-soft);
  }
  .compliments .slip-contacts .group { display: flex; flex-direction: column; gap: 4px; }
  .compliments .slip-contacts .divider { width: 1px; background: #c9d3dc; }
  .compliments .slip-contacts .address-rest { padding-left: 16px; white-space: nowrap; }
  .compliments .band { height: 16px; }

  /* Letterhead */
  .letterhead { left: 640px; top: 40px; width: 520px; height: 707px; }
  .letterhead .wordmark { position: absolute; left: 0; right: 0; top: 60px; justify-content: center; font-size: 40px; }
  .letterhead .wordmark .mark-square { width: 30px; height: 30px; }
  .letterhead .letter-body {
    position: absolute; left: 56px; right: 56px; top: 210px;
    font-size: 11.5px; line-height: 1.9; color: var(--ink-soft);
  }
  .letterhead .letter-body p + p { margin-top: 18px; }
  .letterhead .letter-footer {
    position: absolute; left: 0; right: 0; bottom: 30px; height: 58px;
    padding: 0 18px;
    background: var(--paper-tint);
    display: flex; align-items: center; justify-content: center;
    font-size: 9.5px; color: var(--ink);
    white-space: nowrap;
  }
  .letterhead .letter-footer .item { white-space: nowrap; }
  .letterhead .letter-footer b { color: var(--brand-navy); font-weight: 600; margin-right: 3px; }
  .letterhead .letter-footer .sep { color: var(--ink-soft); margin: 0 5px; }
  .letterhead .band { height: 30px; }

  /* Business cards */
  .card { top: 800px; width: 420px; height: 240px; }
  .card-front { left: 120px; background: var(--paper-tint); }
  .card-front .wordmark { position: absolute; right: 34px; top: 34px; font-size: 32px; }
  .card-front .wordmark .mark-square { width: 24px; height: 24px; }
  .card-front .holder { position: absolute; left: 34px; top: 100px; }
  .card-front .holder-name { font-size: 15px; font-style: italic; font-weight: 600; color: var(--brand-navy); }
  .card-front .holder-role { font-size: 10px; color: var(--ink-soft); margin-bottom: 8px; }
  .card-front .holder .contact-line { font-size: 10px; color: var(--ink-soft); margin-top: 3px; }
  .card-front .band { height: 16px; }
  .card-back { left: 660px; background: var(--brand-sky); }
  .card-back .wordmark { position: absolute; inset: 0; justify-content: center; font-size: 38px; }
  .card-back .wordmark .mark-square { width: 28px; height: 28px; }
</style>
</head>
<body>
<svg width="0" height="0" style="position:absolute" aria-hidden="true">
  <symbol id="icon-pin" viewBox="0 0 10 10"><path d="M5 0a3.4 3.4 0 0 0-3.4 3.4C1.6 6 5 10 5 10s3.4-4 3.4-6.6A3.4 3.4 0 0 0 5 0zm0 4.8a1.4 1.4 0 1 1 0-2.8 1.4 1.4 0 0 1 0 2.8z"/></symbol>
  <symbol id="icon-phone" viewBox="0 0 10 10"><path d="M2.1 0.5l1.6 1.7-0.9 1.2a6 6 0 0 0 3.8 3.8l1.2-0.9 1.7 1.6-1 1.6C4.7 9.5 0.5 5.3 0.5 1.5z"/></symbol>
  <symbol id="icon-globe" viewBox="0 0 10 10"><path d="M5 0.5a4.5 4.5 0 1 0 0 9 4.5 4.5 0 0 0 0-9zm0 1a3.5 3.5 0 0 1 3.4 3H1.6A3.5 3.5 0 0 1 5 1.5zM1.6 5.5h6.8a3.5 3.5 0 0 1-6.8 0z"/></symbol>
  <symbol id="icon-mail" viewBox="0 0 10 10"><path d="M0.5 2h9v6h-9zm1 1v0.4L5 5.6l3.5-2.2V3z"/></symbol>
</svg>

<section class="sheet envelope" aria-label="Envelope">
  <div class="wordmark"><span class="mark-square"></span>Sumvera</div>
  <div class="return-address contact-line"><svg class="icon"><use href="#icon-pin"/></svg>Dummy city, Dummy country, land</div>
  <div class="band"></div>
</section>

<section class="sheet compliments" aria-label="Compliments slip">
  <div class="wordmark"><span class="mark-square"></span>Sumvera</div>
  <div class="slip-contacts">
    <div class="group">
      <div class="contact-line"><svg class="icon"><use href="#icon-phone"/></svg>123-456-7890</div>
      <div class="contact-line"><svg class="icon"><use href="#icon-globe"/></svg>www.sumvera.com</div>
      <div class="contact-line"><svg class="icon"><use href="#icon-mail"/></svg>john@sumvera.com</div>
    </div>
    <div class="divider"></div>
    <div class="group">
      <div class="contact-line"><svg class="icon"><use href="#icon-pin"/></svg>Dummy city</div>
      <div class="address-rest">Dummy country, land</div>
    </div>
  </div>
  <div class="slip-title">WITH COMPLEMENTS</div>
  <div class="band"></div>
</section>

<section class="sheet letterhead" aria-label="Letterhead">
  <div class="wordmark"><span class="mark-square"></span>Sumvera</div>
  <div class="letter-body">
    <p>Lorem ipsum dolor sit amet, consectetur adipiscing elit. Sed at ante. Mauris eleifend, quam a vulputate dictum, massa eget vulputate orci purus ut lorem. In fringilla mi in ligula. Pellentesque adipiscing. Sed quamodio, tempus ac, aliquam molestie varius ac, tellus. Vivamus rutrum interdum. Pellentesque lorem.</p>
    <p>Curabitur sit amet erat quis risus feugiat viverra. Pellentesque augue justo, sagittis et, lacinia at, venenatis non, dictum risus. Etiam tristique nisl a nulla. Ut a orci. Curabitur malesuada nec, magna. Nulla facilisi. Nunc volutpat. Vestibulum ante ipsum ultrices posuere cubilia Curae; Ut sit amet orci vel mauris blandit dignissim viverra velit. Curabitur in odio.</p>
  </div>
  <div class="letter-footer">
    <span class="item"><b>E:</b>john@sumvera.com</span><span class="sep">|</span>
    <span class="item"><b>T:</b>123-456-7890</span><span class="sep">|</span>
    <span class="item"><b>W:</b>www.sumvera.com</span><span class="sep">|</span>
    <span class="item"><b>A:</b>Dummy city, Dummy country, land</span>
  </div>
  <div class="band"></div>
</section>

<section class="sheet card card-front" aria-label="Business card front">
  <div class="wordmark"><span class="mark-square"></span>Sumvera</div>
  <div class="holder">
    <div class="holder-name">John Doe</div>
    <div class="holder-role">Director</div>
    <div class="contact-line"><svg class="icon"><use href="#icon-phone"/></svg>123-456-7890</div>
    <div class="contact-line"><svg class="icon"><use href="#icon-globe"/></svg>www.sumvera.com</div>
    <div class="contact-line"><svg class="icon"><use href="#icon-mail"/></svg>john@sumvera.com</div>
    <div class="contact-line"><svg class="icon"><use href="#icon-pin"/></svg>Dummy city, Dummy country, land</div>
  </div>
  <div class="band"></div>
</section>

<section class="sheet card card-back" aria-label="Business card back">
  <div class="wordmark wordmark--white"><span class="mark-square"></span>Sumvera</div>
</section>
</body>
</html>
```